New webpage design for Talvora.se, participant management system informationpage.

Project Brief: New Website Design for Talvora.se (Participant Management System)
About Talvora.se:
Talvora.se is an established participant management system used by organizations and course providers in Sweden to handle event and course registrations. Our website’s primary audience is course providers, event organizers, and potential users seeking efficient management tools.
Project Goal:
We are launching a new public-facing website for Talvora.se, which will present information about our system, features, FAQ, pricing, news, testimonials, and more. The new site will be built in Umbraco CMS and should follow our visual identity as described in the attached graphic manual.
Deliverables:
We need complete, modern, and responsive page designs (desktop and mobile) for the following pages:
- Home page (landing page)
- Features page
- FAQ page
- About Us page
- Contact Us / Book a Demo page
- Pricing page
- Testimonials page
- News / Blog page
Design Guidelines:
- Please use the attached Plomvik graphic manual for guidance (Plomvik is a sister project; use the same branding).
- The Talvora.se logo is attached and must be included.
- Please use the blue color palette variant from the guide.
- Typography and graphic elements should be consistent with the manual.
- Designs must be suitable for implementation in Umbraco CMS (avoid overly complex layouts or animations that might be difficult to develop).
- All designs should be responsive and work well on desktop, tablet, and mobile.
- Final deliverables should be provided in Figma or Adobe XD (preferably Figma).
What We Like:
- Clean, modern, Scandinavian style.
- Clear navigation and strong hierarchy.
- Readable, accessible layouts.
What to Avoid:
- Overly playful or cartoonish elements.
- Too much clutter or excessive graphical elements.
- Dark color schemes (please focus on blue/light).
References:
- Our current site: https://talvora-demo.se
- Graphic manual (see attachment)
- Talvora logo (see attachment)
Additional Notes:
- The new design should improve clarity, usability, and visual appeal compared to our current site.
- Feel free to suggest visual improvements, but remain consistent with our brand guidelines.
Other font styles liked:
- Orev and Cabin. See attached font files

```html
<!DOCTYPE html>
<html lang="en">
<head>
<meta charset="utf-8">
<title>Talvora.se – Participant Management System</title>
<link href="https://fonts.googleapis.com/css2?family=Saira:wght@400;500;600&family=Cabin:wght@400;500;600;700&display=swap" rel="stylesheet">
<style>
:root{
  --navy:#0a3557;
  --deep:#0d4c7a;
  --blue:#1f9ad9;
  --sky:#34aee8;
  --pale:#a9dcf5;
  --mist:#eaf7fd;
  --ink:#4a5560;
  --muted:#7c8690;
  --line:#c8cdd2;
  --white:#ffffff;
}
*{margin:0;padding:0;box-sizing:border-box}
html,body{width:1200px;height:4190px;overflow:hidden;background:var(--white)}
body{font-family:"Cabin",sans-serif;color:var(--ink);position:relative}
.abs{position:absolute}
.heading{font-family:"Saira",sans-serif;font-weight:500;color:var(--blue);font-size:40px;letter-spacing:.5px;line-height:1}
.center{left:0;width:1200px;text-align:center}
.rule{height:3px;background:var(--blue)}
.divider{left:311px;width:578px;height:1px;background:var(--line)}
.btn{display:flex;align-items:center;justify-content:center;background:var(--sky);color:var(--white);font-size:10px;font-weight:500;letter-spacing:.5px;text-transform:uppercase}
.body-text{font-size:10.5px;line-height:15px;color:var(--muted)}
.ph{display:block}

/* hero */
.hero{left:0;top:0;width:1200px;height:512px;background:radial-gradient(ellipse at 78% 55%,#5d95c4 0%,#2f6fa3 28%,#155b8d 55%,#0b4575 100%)}
.logo{font-family:"Cabin",sans-serif;font-weight:500;color:var(--white);font-size:26px;letter-spacing:.5px}
.nav{top:30px;left:365px;display:flex;gap:31px;font-size:9px;color:var(--white)}
.hero-title{left:160px;top:100px;font-family:"Saira",sans-serif;font-weight:500;font-size:45px;line-height:45px;color:#bfe6fb;letter-spacing:1px}
.hero-text{left:161px;top:224px;width:460px;font-size:9.6px;line-height:14.2px;color:var(--white)}

/* about */
.frame{background:var(--pale)}
.chart-panel{background:var(--white)}

/* features */
.feature-img{height:200px;position:relative}
.feature-label{position:absolute;left:0;bottom:0;width:100%;height:36px;background:rgba(52,174,232,.55);color:var(--white);font-family:"Saira",sans-serif;font-size:17px;letter-spacing:2px;display:flex;align-items:center;justify-content:center;text-transform:uppercase}

/* plans */
.plans{left:0;top:1597px;width:1200px;height:736px;background:var(--mist)}
.plan{background:var(--white);border-radius:6px}
.plan-head{height:46px;display:flex;background:var(--navy);border-radius:6px 6px 0 0;overflow:hidden}
.plan-name{flex:1;padding-left:22px;display:flex;align-items:center;font-family:"Saira",sans-serif;font-size:25px;font-weight:500;color:var(--white);letter-spacing:.5px}
.plan-price{width:66px;background:var(--sky);color:var(--white);text-align:center;font-family:"Saira",sans-serif;font-size:21px;line-height:20px;padding-top:5px}
.plan-price small{display:block;font-size:6.5px;letter-spacing:1px;line-height:8px}
.plan-list{list-style:none;position:absolute;left:22px}
.plan-list li{height:32.5px;display:flex;align-items:center;gap:19px;font-size:10px;color:var(--muted);text-transform:uppercase;letter-spacing:.3px}
.tick{width:17px;height:17px;border-radius:50%;background:var(--blue);flex:none}
.tick.off{background:#d9dcdf}
.pill{border-radius:16px;height:30px;width:127px}

/* testimonials */
.t-card{border:1px solid #d5dadf;background:var(--white);width:278px;height:175px}
.t-avatar{width:38px;height:38px;border-radius:50%}
.t-name{font-size:14px;font-weight:500;color:var(--blue)}
.t-date{font-size:8px;color:var(--muted)}
.stars{font-size:10px;color:#f5b400;letter-spacing:2px}
.dot{width:17px;height:17px;border-radius:50%;border:1px solid var(--blue);display:flex;align-items:center;justify-content:center}
.dot i{width:9px;height:9px;border-radius:50%;background:var(--blue)}
.dot.idle{border-color:var(--pale)}.dot.idle i{background:var(--pale)}
.quote{font-family:"Saira",sans-serif;font-size:130px;color:#d7dadd;line-height:1;font-weight:600}

/* footer */
.footer{left:0;top:3761px;width:1200px;height:429px;background:radial-gradient(ellipse at 70% 60%,#2f79b0 0%,#15598c 45%,#0b3f68 100%)}
.f-title{font-size:9px;font-weight:700;color:var(--white)}
.f-links{list-style:none;font-size:9px;color:var(--white)}
.f-links li{height:23.5px}
.social{width:23px;height:23px;border-radius:50%;background:var(--white)}
.bottom-bar{left:0;top:4156px;width:1200px;height:34px;background:#1f8fd0;display:flex;align-items:center}
</style>
</head>
<body>

<!-- HERO -->
<section class="abs hero" role="img" aria-label="Hand holding glowing arrows and gears over a blue digital background"></section>
<div class="abs logo" style="left:160px;top:18px">talvora.</div>
<nav class="abs nav"><span>About Us</span><span>Features</span><span>Pricing</span><span>Testimonials</span><span>Blog</span><span>Contact Us</span></nav>
<div class="abs" style="left:932px;top:30px;font-size:9px;color:#fff;display:flex;align-items:center;gap:6px">
  <svg width="9" height="9" viewBox="0 0 10 10"><circle cx="4" cy="4" r="3" fill="none" stroke="#fff" stroke-width="1.3"/><line x1="6.3" y1="6.3" x2="9" y2="9" stroke="#fff" stroke-width="1.3"/></svg>Search
</div>
<div class="abs" style="left:1012px;top:30px;font-size:9px;color:#fff;display:flex;gap:8px;align-items:center">En
  <svg width="7" height="5" viewBox="0 0 7 5"><path d="M1 1l2.5 2.5L6 1" stroke="#fff" fill="none" stroke-width="1.2"/></svg>
</div>
<h1 class="abs hero-title">Participant<br>Management System</h1>
<p class="abs hero-text">Lorem Ipsum is simply dummy text of the printing and typesetting industry. Lorem Ipsum has been the industry's standard dummy text ever since the 1500s, when an unknown printer took a galley of type and scrambled it to make a type specimen book. It has survived not only five centuries, but also the leap into electronic typesetting, remaining essentially unchanged. It was popularised in the 1960s with the release of Typeset sheets containing Lorem Ipsum passages, and more recently with desktop publishing software like Folio PageSetter including versions of Lorem Ipsum.</p>
<div class="abs btn" style="left:161px;top:366px;width:127px;height:34px">Read More</div>

<!-- ABOUT -->
<h2 class="abs heading" style="left:160px;top:574px">About Us</h2>
<div class="abs rule" style="left:161px;top:626px;width:172px"></div>
<p class="abs body-text" style="left:161px;top:658px;width:280px;font-size:10.5px">Talvora.se is an established participant management system used by organizations and course providers in Sweden to handle event and course registrations. Our website's primary audience is course providers, event organizers, and potential users seeking efficient management tools.</p>
<div class="abs btn" style="left:161px;top:785px;width:127px;height:33px">See More</div>

<div class="abs frame" style="left:509px;top:553px;width:145px;height:30px"></div>
<div class="abs frame" style="left:509px;top:553px;width:14px;height:40px"></div>
<div class="abs frame" style="left:890px;top:553px;width:149px;height:387px"></div>
<div class="abs" style="left:890px;top:567px;width:135px;height:357px;background:#fff"></div>
<div class="abs chart-panel" style="left:533px;top:577px;width:478px;height:342px;box-shadow:0 0 0 1px #eef2f5"></div>
<div class="abs ph" role="img" aria-label="Business dashboard charts floating over a laptop" style="left:533px;top:577px;width:478px;height:260px;background:linear-gradient(135deg,#2b5e8c,#6f9cc3 55%,#b9d3e6)"></div>
<div class="abs" style="left:818px;top:845px;font-size:8px;color:var(--blue)">Lorem Ipsum</div>
<svg class="abs" style="left:818px;top:858px" width="160" height="52" viewBox="0 0 160 52">
  <g font-family="Cabin,sans-serif" font-size="7" fill="#1f9ad9"><text x="5" y="8">2016</text><text x="5" y="18">2017</text><text x="5" y="28">2018</text><text x="5" y="38">2019</text></g>
  <g fill="#34aee8"><rect x="28" y="4" width="108" height="4"/><rect x="28" y="14" width="66" height="4"/><rect x="28" y="24" width="126" height="4"/><rect x="28" y="34" width="92" height="4"/></g>
</svg>
<div class="abs frame" style="left:447px;top:758px;width:377px;height:250px"></div>
<div class="abs" style="left:462px;top:772px;width:347px;height:221px;background:#fff"></div>
<div class="abs ph" role="img" aria-label="Three colleagues talking in a bright office" style="left:471px;top:780px;width:329px;height:205px;background:linear-gradient(135deg,#e4e6e8,#b9b3ac 50%,#6a5f57)"></div>

<div class="abs divider" style="top:1050px"></div>

<!-- FEATURES -->
<h2 class="abs heading center" style="top:1085px">Features Categories</h2>
<div class="abs rule" style="left:516px;top:1146px;width:225px"></div>

<div class="abs" style="left:161px;top:1185px;width:276px">
  <div class="feature-img" role="img" aria-label="Course provider working at a laptop with a colleague" style="background:linear-gradient(135deg,#e9ecef,#a9a39d 55%,#5a5450)"><div class="feature-label">Course Providers</div></div>
</div>
<div class="abs" style="left:462px;top:1185px;width:276px">
  <div class="feature-img" role="img" aria-label="Event organizers planning at a wall of sticky notes" style="background:linear-gradient(135deg,#3e5a78,#8fa7bd 50%,#4b5f70)"><div class="feature-label">Event Organizers</div></div>
</div>
<div class="abs" style="left:761px;top:1185px;width:276px">
  <div class="feature-img" role="img" aria-label="Hand touching digital management tool icons" style="background:linear-gradient(135deg,#7d5a48,#a8b4bd 50%,#6d8aa0)"><div class="feature-label">Management Tools</div></div>
</div>
<p class="abs body-text" style="left:161px;top:1405px;width:232px">Lorem Ipsum is simply dummy text of the printing and typesetting industry. Lorem Ipsum has been the industry's standard dummy text ever since the 1500s, when an unknown printer took a galley of type and scrambled it to make a type specimen book.</p>
<p class="abs body-text" style="left:462px;top:1405px;width:232px">Lorem Ipsum is simply dummy text of the printing and typesetting industry. Lorem Ipsum has been the industry's standard dummy text ever since the 1500s, when an unknown printer took a galley of type and scrambled it to make a type specimen book.</p>
<p class="abs body-text" style="left:761px;top:1405px;width:232px">Lorem Ipsum is simply dummy text of the printing and typesetting industry. Lorem Ipsum has been the industry's standard dummy text ever since the 1500s, when an unknown printer took a galley of type and scrambled it to make a type specimen book.</p>
<div class="abs btn" style="left:161px;top:1514px;width:127px;height:31px;text-transform:none;font-size:10px">Read More</div>
<div class="abs btn" style="left:462px;top:1514px;width:127px;height:31px;text-transform:none;font-size:10px">Read More</div>
<div class="abs btn" style="left:761px;top:1514px;width:127px;height:31px;text-transform:none;font-size:10px">Read More</div>

<!-- PLANS -->
<section class="abs plans"></section>
<h2 class="abs heading center" style="top:1648px">Our Plans</h2>
<div class="abs rule" style="left:544px;top:1700px;width:115px"></div>

<div class="abs plan" style="left:161px;top:1797px;width:276px;height:392px">
  <div class="plan-head"><div class="plan-name">BASIC</div><div class="plan-price">$25<small>/MONTH</small></div></div>
  <ul class="plan-list" style="top:67px">
    <li><span class="tick"></span>Lorem Ipsum is simply dummy text</li>
    <li><span class="tick"></span>Lorem Ipsum is simply dummy text</li>
    <li><span class="tick"></span>Lorem Ipsum is simply dummy text</li>
    <li><span class="tick off"></span>Lorem Ipsum is simply dummy text</li>
    <li><span class="tick off"></span>Lorem Ipsum is simply dummy text</li>
    <li><span class="tick off"></span>Lorem Ipsum is simply dummy text</li>
    <li><span class="tick off"></span>Lorem Ipsum is simply dummy text</li>
  </ul>
  <div class="abs btn pill" style="left:75px;top:320px;background:var(--pale)">Buy Now</div>
</div>

<div class="abs plan" style="left:462px;top:1736px;width:276px;height:508px;box-shadow:0 6px 10px rgba(0,0,0,.25)">
  <div class="plan-head" style="height:53px"><div class="plan-name" style="font-size:27px">STANDARD</div><div class="plan-price" style="width:76px;padding-top:8px">$40<small>/MONTH</small></div></div>
  <ul class="plan-list" style="top:63px">
    <li style="height:32px"><span class="tick"></span>Lorem Ipsum is simply dummy text</li>
    <li style="height:32px"><span class="tick"></span>Lorem Ipsum is simply dummy text</li>
    <li style="height:32px"><span class="tick"></span>Lorem Ipsum is simply dummy text</li>
    <li style="height:32px"><span class="tick"></span>Lorem Ipsum is simply dummy text</li>
    <li style="height:32px"><span class="tick"></span>Lorem Ipsum is simply dummy text</li>
    <li style="height:32px"><span class="tick"></span>Lorem Ipsum is simply dummy text</li>
    <li style="height:32px"><span class="tick"></span>Lorem Ipsum is simply dummy text</li>
    <li style="height:32px"><span class="tick off"></span>Lorem Ipsum is simply dummy text</li>
    <li style="height:32px"><span class="tick off"></span>Lorem Ipsum is simply dummy text</li>
  </ul>
  <div class="abs btn pill" style="left:75px;top:381px;background:var(--blue)">Buy Now</div>
</div>

<div class="abs plan" style="left:761px;top:1797px;width:276px;height:392px">
  <div class="plan-head"><div class="plan-name">PREMIUM</div><div class="plan-price">$55<small>/MONTH</small></div></div>
  <ul class="plan-list" style="top:65px">
    <li style="height:31px"><span class="tick"></span>Lorem Ipsum is simply dummy text</li>
    <li style="height:31px"><span class="tick"></span>Lorem Ipsum is simply dummy text</li>
    <li style="height:31px"><span class="tick"></span>Lorem Ipsum is simply dummy text</li>
    <li style="height:31px"><span class="tick"></span>Lorem Ipsum is simply dummy text</li>
    <li style="height:31px"><span class="tick"></span>Lorem Ipsum is simply dummy text</li>
    <li style="height:31px"><span class="tick"></span>Lorem Ipsum is simply dummy text</li>
    <li style="height:31px"><span class="tick"></span>Lorem Ipsum is simply dummy text</li>
  </ul>
  <div class="abs btn pill" style="left:75px;top:320px;background:var(--sky)">Buy Now</div>
</div>

<!-- TESTIMONIALS -->
<div class="abs divider" style="top:2335px"></div>
<h2 class="abs heading center" style="top:2370px">Our Client Testimonials</h2>
<div class="abs rule" style="left:473px;top:2435px;width:257px"></div>
<div class="abs quote" style="left:158px;top:2398px">&ldquo;</div>
<div class="abs quote" style="left:975px;top:2655px">&rdquo;</div>

<div class="abs t-card" style="left:161px;top:2483px">
  <div class="abs t-avatar" role="img" aria-label="Client portrait" style="left:17px;top:14px;background:linear-gradient(135deg,#c9b4a8,#7a4a3c)"></div>
  <div class="abs t-name" style="left:77px;top:21px">J.Holm</div>
  <div class="abs t-date" style="left:77px;top:40px">August 10, 2025</div>
  <div class="abs" style="left:244px;top:19px;width:16px;height:16px;border-radius:50%;background:var(--pale)"></div>
  <div class="abs stars" style="left:17px;top:62px">★★★★★</div>
  <p class="abs body-text" style="left:17px;top:80px;width:240px;font-size:9px;line-height:13.5px">Lorem Ipsum is simply dummy text of the printing and typesetting industry. Lorem Ipsum has been the industry's standard dummy text ever since the 1500s.</p>
  <div class="abs" style="left:17px;top:148px;font-size:8px;color:var(--muted)">Read More</div>
</div>
<div class="abs t-card" style="left:461px;top:2483px">
  <div class="abs t-avatar" role="img" aria-label="Client portrait" style="left:17px;top:14px;background:linear-gradient(135deg,#e9d7c9,#d9487d)"></div>
  <div class="abs t-name" style="left:78px;top:21px">Maja Berglund</div>
  <div class="abs t-date" style="left:78px;top:40px">August 2, 2025</div>
  <div class="abs" style="left:244px;top:19px;width:16px;height:16px;border-radius:50%;background:var(--pale)"></div>
  <div class="abs stars" style="left:19px;top:62px">★★★★★</div>
  <p class="abs body-text" style="left:19px;top:80px;width:240px;font-size:9px;line-height:13.5px">Lorem Ipsum is simply dummy text of the printing and typesetting industry. Lorem Ipsum has been the industry's standard dummy text ever since the 1500s.</p>
  <div class="abs" style="left:19px;top:148px;font-size:8px;color:var(--muted)">Read More</div>
</div>
<div class="abs t-card" style="left:760px;top:2483px">
  <div class="abs t-avatar" role="img" aria-label="Client portrait" style="left:22px;top:14px;background:linear-gradient(135deg,#b8a89d,#4c4340)"></div>
  <div class="abs t-name" style="left:79px;top:21px">J.Holm</div>
  <div class="abs t-date" style="left:79px;top:40px">August 10, 2025</div>
  <div class="abs" style="left:245px;top:19px;width:16px;height:16px;border-radius:50%;background:var(--pale)"></div>
  <div class="abs stars" style="left:20px;top:62px">★★★★★</div>
  <p class="abs body-text" style="left:20px;top:80px;width:240px;font-size:9px;line-height:13.5px">Lorem Ipsum is simply dummy text of the printing and typesetting industry. Lorem Ipsum has been the industry's standard dummy text ever since the 1500s.</p>
  <div class="abs" style="left:20px;top:148px;font-size:8px;color:var(--muted)">Read More</div>
</div>
<div class="abs dot" style="left:573px;top:2724px"><i></i></div>
<div class="abs dot idle" style="left:602px;top:2724px"><i></i></div>

<!-- BLOGS -->
<div class="abs divider" style="top:2774px"></div>
<h2 class="abs heading center" style="top:2820px">Our Blogs</h2>
<div class="abs rule" style="left:544px;top:2874px;width:115px"></div>

<div class="abs" style="left:184px;top:2950px;width:203px;height:210px;background:var(--blue)"></div>
<div class="abs ph" role="img" aria-label="Man working on a laptop in a cafe" style="left:161px;top:2969px;width:203px;height:207px;background:linear-gradient(135deg,#3c2e28,#8a5e4c 50%,#c79a8a)"></div>
<p class="abs body-text" style="left:161px;top:3185px;width:200px;font-size:9px;line-height:12px">Lorem Ipsum is simply dummy text of the printing and typesetting industry. Lorem Ipsum has been the industry's standard dummy text ever since the 1500s, when an unknown printer took a galley of type and scrambled it to make a type specimen book.</p>
<div class="abs" style="left:161px;top:3278px;width:203px;text-align:center;font-size:10px;letter-spacing:1.5px;color:var(--ink)">Aug 8, 2025</div>
<div class="abs btn" style="left:198px;top:3307px;width:128px;height:28px;text-transform:none">Read More</div>

<div class="abs" style="left:439px;top:2911px;width:322px;height:504px;background:var(--pale)"></div>
<div class="abs ph" role="img" aria-label="Smiling woman reading on her phone" style="left:462px;top:2932px;width:276px;height:284px;background:linear-gradient(135deg,#5a3a2a,#b4784e 45%,#e9a93a)"></div>
<p class="abs" style="left:462px;top:3226px;width:282px;font-size:8.7px;line-height:12px;color:var(--white)">Lorem Ipsum is simply dummy text of the printing and typesetting industry. Lorem Ipsum has been the industry's standard dummy text ever since the 1500s, when an unknown printer took a galley of type and scrambled it to make a type specimen book. It has survived not only five centuries, but also the leap into electronic typesetting, remaining essentially unchanged.</p>
<div class="abs" style="left:439px;top:3322px;width:322px;text-align:center;font-size:10px;letter-spacing:1.5px;color:var(--blue)">Aug 8, 2025</div>
<div class="abs btn" style="left:536px;top:3353px;width:128px;height:28px;text-transform:none;background:var(--blue)">Read More</div>

<div class="abs" style="left:813px;top:2950px;width:203px;height:210px;background:var(--blue)"></div>
<div class="abs ph" role="img" aria-label="Woman smiling while on a phone call at a laptop" style="left:836px;top:2969px;width:203px;height:207px;background:linear-gradient(135deg,#4b4f55,#b9b4ae 55%,#e8e5e0)"></div>
<p class="abs body-text" style="left:836px;top:3185px;width:203px;font-size:9px;line-height:12px">Lorem Ipsum is simply dummy text of the printing and typesetting industry. Lorem Ipsum has been the industry's standard dummy text ever since the 1500s, when an unknown printer took a galley of type and scrambled it to make a type specimen book.</p>
<div class="abs" style="left:836px;top:3278px;width:203px;text-align:center;font-size:10px;letter-spacing:1.5px;color:var(--ink)">Aug 8, 2025</div>
<div class="abs btn" style="left:873px;top:3307px;width:128px;height:28px;text-transform:none">Read More</div>

<div class="abs dot" style="left:573px;top:3447px"><i></i></div>
<div class="abs dot idle" style="left:602px;top:3447px"><i></i></div>

<!-- NEWSLETTER -->
<div class="abs divider" style="top:3496px"></div>
<h2 class="abs heading center" style="top:3542px">Newsletter</h2>
<p class="abs center" style="top:3614px;font-size:10.5px;color:var(--muted)">Lorem Ipsum is simply dummy text of the printing and typesetting industry.</p>
<div class="abs" style="left:237px;top:3663px;width:501px;height:53px;border:1.5px solid var(--sky);border-radius:4px;display:flex;align-items:center;padding-left:20px;font-size:11px;font-weight:500;color:var(--deep)">Enter your email</div>
<div class="abs btn" style="left:750px;top:3663px;width:213px;height:53px;border-radius:4px;background:var(--blue);font-size:12px;text-transform:none;font-weight:600">Subscribe Now</div>

<!-- FOOTER -->
<footer class="abs footer" role="img" aria-label="Dark blue background of hands typing on a laptop"></footer>
<div class="abs logo" style="left:161px;top:3826px">talvora.</div>
<p class="abs" style="left:163px;top:3880px;width:280px;font-size:9.6px;line-height:18.8px;color:var(--white)">Talvora.se is an established participant management system used by organizations and course providers in Sweden to handle event and course registrations. Our website's primary audience is course providers, event organizers, and potential users seeking efficient management tools.</p>
<div class="abs social" style="left:164px;top:4025px"></div>
<div class="abs social" style="left:205px;top:4025px"></div>
<div class="abs social" style="left:246px;top:4025px"></div>
<div class="abs social" style="left:287px;top:4025px"></div>

<div class="abs f-title" style="left:613px;top:3839px">Quick Links</div>
<ul class="abs f-links" style="left:613px;top:3882px">
  <li>About Us</li><li>Features</li><li>Pricing</li><li>Testimonials</li><li>Blog</li>
</ul>

<div class="abs f-title" style="left:862px;top:3839px">Contact Info</div>
<svg class="abs" style="left:862px;top:3871px" width="9" height="12" viewBox="0 0 9 12"><path d="M4.5 0C2 0 0 2 0 4.4 0 7.7 4.5 12 4.5 12S9 7.7 9 4.4C9 2 7 0 4.5 0z" fill="#fff"/><circle cx="4.5" cy="4.4" r="1.6" fill="#15598c"/></svg>
<div class="abs" style="left:885px;top:3872px;width:160px;font-size:9px;line-height:11px;color:#fff">Talvora.se<br>Lorem Ipsum is simply dummy text of the printing and typesetting industry.</div>
<svg class="abs" style="left:862px;top:3947px" width="10" height="8" viewBox="0 0 10 8"><rect width="10" height="8" rx="1" fill="#fff"/><path d="M0.5 0.8L5 4.5l4.5-3.7" stroke="#15598c" fill="none"/></svg>
<div class="abs" style="left:885px;top:3945px;font-size:9px;color:#fff">info@talvora.com</div>
<svg class="abs" style="left:862px;top:3983px" width="10" height="10" viewBox="0 0 10 10"><path d="M2 0.5l2 2.2-1 1.3c.6 1.3 1.6 2.3 2.9 2.9l1.3-1 2.3 2-1 1.6C4.6 9.3.7 5.4.5 1.5z" fill="#fff"/></svg>
<div class="abs" style="left:885px;top:3982px;font-size:9px;color:#fff">+1234567890</div>

<div class="abs bottom-bar">
  <span style="margin-left:161px;font-size:10px;color:#fff">© 2025Talvora.Se All Rights Reserved.</span>
</div>
<div class="abs social" style="left:933px;top:4164px;width:17px;height:17px"></div>
<div class="abs social" style="left:963px;top:4164px;width:17px;height:17px"></div>
<div class="abs social" style="left:993px;top:4164px;width:17px;height:17px"></div>
<div class="abs social" style="left:1022px;top:4164px;width:17px;height:17px"></div>

</body>
</html>
```